Cover for book on creating escape rooms for educational purposes

A small business (cipher vault academy) needs a book cover design for a new book they are launching as a how-to guide to create educational escape rooms. The target audience is for educators wanting to better engage their students of all ages (Primary, Secondary, Tertiary, Corporate Training).
Book Title: Boundless Classrooms
Sub Title: Harnessing the thrill of puzzle games to make teaching memorable
Authors: Dr Martin and Helen Blake

Book is to be sold on Brindlecart books as a Pagelume eBook and hard copy

Target Market(s)

Educators/Teachers

Industry/Entity Type

Education

Requirements
Must have
• Cipher Vault Academy Logo
Should not have
• A focus only on children

```html
<!DOCTYPE html>
<html lang="en">
<head>
<meta charset="utf-8">
<title>Boundless Classrooms — Book Cover</title>
<link rel="stylesheet" href="https://fonts.googleapis.com/css2?family=Montserrat:wght@300;400&display=swap">
<style>
  :root {
    --plum: #35273f;
    --plum-ink: #33253f;
    --teal: #2fe0d2;
    --violet: #b85ee8;
    --sky: #6fb6f0;
    --paper: #ffffff;
    --shadow: rgba(0, 0, 0, 0.45);
  }
  * { margin: 0; padding: 0; box-sizing: border-box; }
  html, body { width: 840px; height: 1200px; overflow: hidden; background: var(--paper); }
  .cover {
    position: relative;
    width: 840px;
    height: 1200px;
    background: var(--paper);
    font-family: "Montserrat", "Helvetica Neue", Arial, sans-serif;
    color: var(--plum-ink);
    overflow: hidden;
  }
  .cover__band {
    position: absolute;
    left: 0; top: 0;
    width: 840px; height: 516px;
    background: var(--plum);
    box-shadow: 0 4px 6px var(--shadow);
  }
  .cover__emblem {
    position: absolute;
    left: 290px; top: 42px;
    width: 292px; height: 376px;
    border-radius: 146px 146px 60px 60px;
    background: radial-gradient(circle at 50% 38%, rgba(47,224,210,0.55) 0%, rgba(111,182,240,0.35) 35%, rgba(184,94,232,0.3) 62%, rgba(53,39,63,0) 78%);
  }
  .cover__title {
    position: absolute;
    left: 0; width: 840px;
    text-align: center;
    font-weight: 300;
    line-height: 1;
    white-space: nowrap;
  }
  .cover__title--top {
    top: 424px;
    font-size: 100px;
    letter-spacing: 4px;
    color: var(--teal);
  }
  .cover__title--bottom {
    top: 514px;
    font-size: 104px;
    letter-spacing: -1px;
    color: var(--plum-ink);
  }
  .cover__subtitle {
    position: absolute;
    left: 0; top: 694px;
    width: 840px;
    text-align: center;
    font-size: 29px;
    font-weight: 400;
    line-height: 34px;
    letter-spacing: 1px;
    color: var(--plum-ink);
  }
  .cover__authors {
    position: absolute;
    left: 0; top: 1096px;
    width: 840px;
    text-align: center;
    font-size: 40px;
    font-weight: 300;
    letter-spacing: 0;
    color: var(--plum-ink);
  }
</style>
</head>
<body>
  <main class="cover">
    <div class="cover__band"></div>
    <div class="cover__emblem" role="img" aria-label="Glowing teal and violet maze in the shape of a human head with a keyhole at its centre, over faint question marks"></div>
    <h1>
      <span class="cover__title cover__title--top">BOUNDLESS</span>
      <span class="cover__title cover__title--bottom">CLASSROOMS</span>
    </h1>
    <p class="cover__subtitle">Harnessing the thrill of puzzle games<br>to make teaching memorable</p>
    <p class="cover__authors">DR MARTIN AND HELEN BLAKE</p>
  </main>
</body>
</html>
```